Tavorin Brand Household Liquids

We need a logo designed, as well as a design concept under the Tavorin brand for dishwashing liquid, liquid handwashing soap and toilet bowl cleanser.

The design concept should be fresh and clean looking using green and blue colors.

The packaging should be targeted to mothers and ladies of the house who do the grocery shopping. It should convey the message that this product will magically clean their hands/ laundry/ whatnots.

Target Market(s)

Middle class to low end market (B,C,D)

Colors
00a990
0592cd
a54499

Requirements
Must have
• Tavorin the "Wizard" who magically removes dust/ germs/ dirt/ bacteria
Nice to have
• A wizard cartoon image on the label
Should not have
• black colors

```html
<!DOCTYPE html>
<html lang="en">
<head>
<meta charset="utf-8">
<title>Tavorin Liquid Handwashing Soap Label</title>
<link rel="stylesheet" href="https://fonts.googleapis.com/css2?family=Baloo+2:wght@800&family=Roboto:wght@500;700;900&display=swap">
<style>
  :root {
    --page-bg: #ecebe8;
    --lime: #a6d62a;
    --lime-light: #d3ef6a;
    --leaf: #5fb41e;
    --leaf-deep: #2f8a12;
    --brand-blue: #0592cd;
    --navy: #16407a;
    --teal: #00a990;
    --plum: #a54499;
    --alert-red: #e2231a;
    --white: #ffffff;
  }
  * { margin: 0; padding: 0; box-sizing: border-box; }
  html, body {
    width: 900px;
    height: 1200px;
    overflow: hidden;
    background: var(--page-bg);
  }
  .canvas {
    position: relative;
    width: 900px;
    height: 1200px;
  }
  .label {
    position: absolute;
    left: 110px;
    top: 130px;
    width: 680px;
    height: 940px;
    border-radius: 28px;
    overflow: hidden;
    background: linear-gradient(180deg, var(--lime-light) 0%, var(--lime) 45%, var(--leaf) 100%);
  }
  .label__waves {
    position: absolute;
    inset: 0;
    width: 100%;
    height: 100%;
  }
  .brand-name {
    position: absolute;
    top: 250px;
    left: 0;
    width: 100%;
    text-align: center;
    font-family: "Baloo 2", sans-serif;
    font-weight: 800;
    font-size: 150px;
    line-height: 1;
    color: var(--brand-blue);
  }
  .brand-tagline {
    position: absolute;
    top: 400px;
    left: 350px;
    font-family: "Roboto", sans-serif;
    font-weight: 500;
    font-style: italic;
    font-size: 22px;
    color: var(--navy);
  }
  .benefits {
    position: absolute;
    top: 450px;
    left: 250px;
    list-style: none;
    font-family: "Roboto", sans-serif;
    font-weight: 900;
    font-size: 30px;
    line-height: 46px;
    color: var(--navy);
  }
  .benefits li {
    display: flex;
    align-items: center;
    gap: 14px;
  }
  .benefits li::before {
    content: "";
    width: 18px;
    height: 18px;
    border-radius: 50%;
    background: var(--brand-blue);
    flex: none;
  }
  .mascot {
    position: absolute;
    left: 0;
    top: 470px;
    width: 230px;
    height: 380px;
    border-radius: 0 120px 40px 0;
    background: linear-gradient(160deg, #6a3d8f 0%, var(--plum) 45%, #e9e4ef 100%);
  }
  .promo {
    position: absolute;
    top: 640px;
    left: 230px;
    width: 420px;
    text-align: center;
    font-family: "Roboto", sans-serif;
    font-weight: 900;
    font-size: 40px;
    color: var(--alert-red);
  }
  .net-contents {
    position: absolute;
    top: 698px;
    left: 230px;
    width: 420px;
    text-align: center;
    font-family: "Roboto", sans-serif;
    font-weight: 700;
    font-size: 22px;
    color: var(--white);
  }
</style>
</head>
<body>
<div class="canvas">
  <section class="label">
    <svg class="label__waves" viewBox="0 0 680 940" preserveAspectRatio="none" aria-hidden="true">
      <defs>
        <radialGradient id="glow" cx="50%" cy="30%" r="50%">
          <stop offset="0%" stop-color="#ffffff" stop-opacity="0.95"/>
          <stop offset="100%" stop-color="#ffffff" stop-opacity="0"/>
        </radialGradient>
        <linearGradient id="skyBand" x1="0" y1="0" x2="0" y2="1">
          <stop offset="0%" stop-color="#0592cd" stop-opacity="0.55"/>
          <stop offset="100%" stop-color="#9fe0f5" stop-opacity="0"/>
        </linearGradient>
      </defs>
      <rect x="0" y="0" width="680" height="260" fill="url(#skyBand)"/>
      <ellipse cx="340" cy="300" rx="360" ry="230" fill="url(#glow)"/>
      <path d="M0 560 C 180 500, 420 640, 680 520 L680 600 C 430 720, 200 580, 0 650 Z" fill="#ffffff" opacity="0.35"/>
      <path d="M0 760 C 200 690, 430 820, 680 700 L680 940 L0 940 Z" fill="#2f8a12" opacity="0.55"/>
      <path d="M0 820 C 220 760, 440 880, 680 780 L680 820 C 430 920, 220 800, 0 870 Z" fill="#d3ef6a" opacity="0.8"/>
      <path d="M0 880 C 230 830, 450 930, 680 850 L680 940 L0 940 Z" fill="#5fb41e"/>
    </svg>

    <h1 class="brand-name">Tavorin</h1>
    <p class="brand-tagline">liquid handwashing soap</p>

    <ul class="benefits">
      <li>99.99% GERMS KILLER</li>
      <li>TOUGHEST BACTERIA REMOVAL</li>
      <li>FIGHTS ODOUR</li>
    </ul>

    <div class="mascot" role="img" aria-label="Cartoon wizard mascot in a purple hat and robe holding a magic wand"></div>

    <p class="promo">NEW &amp; IMPROVED</p>
    <p class="net-contents">Net Contents : 500ml</p>
  </section>
</div>
</body>
</html>
```